The Vixen Rides Again Line of Sparkling Wine & Spirits

Back info: Tara Rose Whitfield Owner 209-555-0143 1480 E. Harlow Rd, Bldg. 7, & 8, Marlow Ca. 95299
Sparkling Wines & Memorabilia www.thevixenridesagain.example
Ok I have uploaded the winning design. The color that I am after is the Fushia, Raspberry, Red, Matte Satin Matalic Finish. With a 24 Karet Gold color Foil. The Bottle is on the top row and it's the 2nd Bottle in. That is the Color that I want. This is the style of font. Make sure that you put what we're advertising. Good Luck to you all. Warmest regards, Tara
Target Market(s)
21 & up UniSex
Industry/Entity Type
Sparkling Wine and Memorabilia
Contact Information for Business Card
there listed up above.....

```html
<!DOCTYPE html>
<html lang="en">
<head>
<meta charset="utf-8">
<title>The Vixen Rides Again – Business Card</title>
<link href="https://fonts.googleapis.com/css2?family=Playfair+Display:wght@900&family=Poppins:wght@400;500;600&display=swap" rel="stylesheet">
<style>
  :root{
    --bg:#262729;
    --fuchsia-hi:#ee1896;
    --fuchsia:#c8127d;
    --raspberry:#8e0e4e;
    --gold:#e2b443;
    --gold-light:#f8e08a;
    --gold-deep:#b8862a;
    --ink:#111;
    --white:#fff;
  }
  *{margin:0;padding:0;box-sizing:border-box}
  html,body{width:1200px;height:952px;overflow:hidden;background:var(--bg)}
  .canvas{position:relative;width:1200px;height:952px}
  .card{
    position:absolute;left:250px;width:700px;height:400px;overflow:hidden;
    background:radial-gradient(ellipse at 42% 45%,var(--fuchsia-hi) 0%,var(--fuchsia) 48%,var(--raspberry) 100%);
    box-shadow:0 18px 40px rgba(0,0,0,.55);
  }
  .card--front{top:36px}
  .card--back{top:516px}
  .card__rule{position:absolute;left:0;top:0;width:700px;height:400px}

  .brand-title{
    position:absolute;left:0;right:0;top:120px;text-align:center;
    font-family:"Playfair Display",serif;font-weight:900;font-size:54px;
    line-height:1.05;color:var(--ink);
  }

  .logo{position:absolute;left:90px;top:48px;width:190px;text-align:center}
  .logo__mark{width:96px;height:96px;border-radius:50%;background:var(--ink);margin:0 auto 14px}
  .logo__name{font-family:"Poppins",sans-serif;font-weight:600;font-size:16px;color:var(--ink);line-height:1.2}

  .contact{position:absolute;left:330px;top:40px;width:355px}
  .contact__name{
    font-family:"Playfair Display",serif;font-weight:900;font-size:40px;
    color:var(--gold);line-height:1;letter-spacing:.5px;white-space:nowrap
  }
  .contact__role{
    font-family:"Poppins",sans-serif;font-size:17px;color:var(--white);
    display:inline-block;margin-top:4px;padding-bottom:4px;border-bottom:1.5px solid var(--white)
  }
  .contact__list{list-style:none;margin-top:16px}
  .contact__item{
    display:flex;align-items:flex-start;gap:10px;margin-bottom:9px;
    font-family:"Poppins",sans-serif;font-size:15px;line-height:1.3;color:var(--white);white-space:nowrap
  }
  .icon{flex:none;width:20px;height:20px;border-radius:4px;background:var(--ink);display:flex;align-items:center;justify-content:center}
  .icon svg{width:13px;height:13px}
  .social{display:flex;gap:8px;margin-top:2px}
  .social__tile{width:20px;height:20px;border-radius:4px;background:linear-gradient(135deg,var(--gold-light),var(--gold-deep))}
  .tagline{font-family:"Poppins",sans-serif;font-weight:600;font-size:12px;color:var(--white);margin-top:8px}
</style>
</head>
<body>
<main class="canvas">

  <section class="card card--front">
    <svg class="card__rule" viewBox="0 0 700 400" aria-hidden="true">
      <defs>
        <linearGradient id="foil" x1="0" x2="1">
          <stop offset="0" stop-color="#b8862a"/><stop offset=".5" stop-color="#f8e08a"/><stop offset="1" stop-color="#c9962e"/>
        </linearGradient>
      </defs>
      <rect x="0" y="316" width="230" height="6" fill="#fff"/>
      <rect x="230" y="326" width="470" height="6" fill="url(#foil)"/>
    </svg>
    <h1 class="brand-title">The Vixen<br>Rides Again</h1>
  </section>

  <section class="card card--back">
    <svg class="card__rule" viewBox="0 0 700 400" aria-hidden="true">
      <defs>
        <linearGradient id="foil2" x1="0" x2="1">
          <stop offset="0" stop-color="#b8862a"/><stop offset=".5" stop-color="#f8e08a"/><stop offset="1" stop-color="#c9962e"/>
        </linearGradient>
      </defs>
      <rect x="0" y="322" width="230" height="6" fill="#fff"/>
      <rect x="230" y="332" width="470" height="6" fill="url(#foil2)"/>
    </svg>

    <div class="logo">
      <div class="logo__mark"></div>
      <div class="logo__name">The Vixen Rides Again</div>
    </div>

    <div class="contact">
      <h2 class="contact__name">Tara Whitfield</h2>
      <span class="contact__role">Owner</span>
      <ul class="contact__list">
        <li class="contact__item">
          <span class="icon"><svg viewBox="0 0 12 12"><path d="M6 1a3.5 3.5 0 0 0-3.5 3.5C2.5 7 6 11 6 11s3.5-4 3.5-6.5A3.5 3.5 0 0 0 6 1zm0 5a1.5 1.5 0 1 1 0-3 1.5 1.5 0 0 1 0 3z" fill="#e2b443"/></svg></span>
          <span>1480 E. Harlow Rd, Bldg. 7, &amp; 8,<br>Marlow Ca. 95299</span>
        </li>
        <li class="contact__item">
          <span class="icon"><svg viewBox="0 0 12 12"><path d="M3 1l2 2.5-1.2 1.3a6 6 0 0 0 3.4 3.4L8.5 7 11 9l-1.3 1.8C5.5 10.5 1.5 6.5 1.2 2.3z" fill="#e2b443"/></svg></span>
          <span>555-555-0143</span>
        </li>
        <li class="contact__item">
          <span class="icon"><svg viewBox="0 0 12 12"><rect x="1" y="2.5" width="10" height="7" fill="none" stroke="#e2b443" stroke-width="1.2"/><path d="M1 2.5l5 4 5-4" fill="none" stroke="#e2b443" stroke-width="1.2"/></svg></span>
          <span>hello@thevixenridesagain.example</span>
        </li>
        <li class="contact__item">
          <span class="icon"><svg viewBox="0 0 12 12"><path d="M2 1l8 4-3.2 1L5.5 10z" fill="#e2b443"/></svg></span>
          <span>www.thevixenridesagain.example</span>
        </li>
      </ul>
      <div class="social"><span class="social__tile"></span><span class="social__tile"></span></div>
      <p class="tagline">Sparkling Wines &amp; Memorabilia</p>
    </div>
  </section>

</main>
</body>
</html>
```